Wedding poster templates PSD format

Create a range of editable wedding templates for different themes. Must be able able to adjust layers and edit all text.
Must include Names and dates for example purposes.
These are to be used as print templates for our wedding clients so we must be able to edit in photoshop.

We would like to see designs will be perfect for our customers to keep as a memento from their wedding or provided as a gift to be kept and remembered

Also needs to specific scale 1250mm high x 450mm wide

We have attached a sample of one of our designs. We would like similar designs to example.

Some attached links also show the style and look we are after.

Some nice silhouette type images to suit the chosen theme.

http://www.velquoriath.com/wp-content/uploads/2012/06/nautical_BrindleFernwick.jpg

http://www.gossamerpennyhollows.com/wp-content/uploads/2012/07/IMG_3168C.jpg

Themes we would like as ideas
Hawaii, Beach, Vintage, Floral, Tropical, Country, Garden, Nautical

Target Market(s)

Wedding

Industry/Entity Type

Wedding

Font styles to use
Decorative

Requirements
Must have
• Theme, Layers, Text, Names example, Dates example
Nice to have
• Silhouettes,
• Word cloud,
• Poem
• Vector images
Should not have
• Too much colour.
• Photographic images

```html
<!DOCTYPE html>
<html lang="en">
<head>
<meta charset="utf-8">
<title>Wedding Invitation Poster – Elaina &amp; Maximillian</title>
<link href="https://fonts.googleapis.com/css2?family=Great+Vibes&family=Antonio:wght@100;200&family=Cutive&family=Parisienne&display=swap" rel="stylesheet">
<style>
  :root{
    --page:#ffffff;
    --paper-top:#f4efe3;
    --paper-bottom:#e6d9bd;
    --stripe:rgba(255,255,255,0.35);
    --gold:#f7cf85;
    --gold-soft:rgba(247,207,133,0.45);
    --ink:#141414;
    --ink-soft:rgba(40,34,28,0.28);
    --rule:#555049;
  }
  *{margin:0;padding:0;box-sizing:border-box}
  html,body{width:1000px;height:1200px;overflow:hidden;background:var(--page)}
  .canvas{position:relative;width:1000px;height:1200px}
  .poster{
    position:absolute;left:321px;top:57px;width:369px;height:1027px;
    background:
      repeating-linear-gradient(90deg,transparent 0 6px,var(--stripe) 6px 9px),
      linear-gradient(180deg,var(--paper-top),var(--paper-bottom));
    overflow:hidden;
  }
  .ribbon{position:absolute;left:0;top:0;width:369px;height:120px}
  .abs{position:absolute;color:var(--ink);white-space:nowrap;font-weight:400}
  .script{font-family:"Great Vibes",cursive}
  .caps{font-family:"Antonio",sans-serif;font-weight:100}
  .type{font-family:"Cutive",serif}
  .italic{font-family:"Parisienne",cursive}

  .swirl-area{
    position:absolute;left:8px;top:150px;width:355px;height:530px;
    border-radius:48% 52% 46% 54% / 40% 44% 56% 60%;
    background:radial-gradient(ellipse at 50% 50%,transparent 45%,var(--gold-soft) 62%,transparent 78%);
  }

  .banner-text{left:60px;top:72px;width:247px;text-align:center;font-size:19px;line-height:24px}
  .bride-first{left:40px;top:214px;font-size:76px;line-height:1}
  .bride-rest{left:42px;top:286px;font-size:33px;line-height:1;letter-spacing:1px}
  .ampersand{left:150px;top:292px;font-size:150px;line-height:1}
  .groom-first{left:62px;top:418px;font-size:62px;line-height:1}
  .groom-rest{left:106px;top:487px;font-size:33px;line-height:1;letter-spacing:1px}

  .rule{position:absolute;left:22px;width:319px;border-top:1px dotted var(--rule)}
  .invite-line{left:0;width:369px;top:706px;text-align:center;font-size:20px}
  .date{left:28px;top:764px;width:76px;text-align:center;font-size:24px;line-height:30px}
  .dots-v{position:absolute;left:130px;top:762px;height:92px;border-left:4px dotted var(--ink)}
  .dots-h{position:absolute;left:149px;top:803px;width:183px;border-top:4px dotted var(--ink)}
  .detail{left:149px;font-size:13px;line-height:18px}
  .detail.time{top:764px}
  .detail.venue{top:817px}
  .follow-line{left:0;width:369px;top:889px;text-align:center;font-size:19px}

  .ornament{position:absolute;background:radial-gradient(ellipse at center,var(--ink-soft),transparent 72%)}
  .ornament.top{left:99px;top:665px;width:170px;height:28px}
  .ornament.bottom{left:119px;top:943px;width:125px;height:65px}
</style>
</head>
<body>
<div class="canvas">
  <section class="poster" aria-label="Wedding invitation">
    <div class="swirl-area" role="img" aria-label="Gold ribbon swirl flourish around the names"></div>

    <svg class="ribbon" viewBox="0 0 369 120" aria-hidden="true">
      <polygon points="20,50 82,50 82,92 20,92 40,71" fill="var(--gold)" stroke="var(--ink)" stroke-width="1"/>
      <polygon points="347,50 285,50 285,92 347,92 327,71" fill="var(--gold)" stroke="var(--ink)" stroke-width="1"/>
      <polygon points="82,50 60,65 82,65" fill="var(--ink)"/>
      <polygon points="285,50 307,65 285,65" fill="var(--ink)"/>
      <path d="M60,65 H307 V102 Q183,110 60,102 Z" fill="var(--gold)" stroke="var(--ink)" stroke-width="1"/>
    </svg>

    <p class="abs italic banner-text">With the Most Joyful Hearts</p>

    <h1 class="abs script bride-first">Elaina</h1>
    <p class="abs caps bride-rest">ROSE HALLER</p>
    <p class="abs script ampersand">&amp;</p>
    <h1 class="abs script groom-first">Maximillian</h1>
    <p class="abs caps groom-rest">OWEN CALLAWAY</p>

    <div class="ornament top" role="img" aria-label="Decorative scroll flourish"></div>

    <div class="rule" style="top:695px"></div>
    <p class="abs italic invite-line">Invite you to celebrate their marriage</p>
    <div class="rule" style="top:740px"></div>

    <p class="abs type date">Nov.<br>11<br>2016</p>
    <div class="dots-v"></div>
    <p class="abs type detail time">Three O’clock in<br>the afternoon</p>
    <div class="dots-h"></div>
    <p class="abs type detail venue">Casa Lirio<br>Alderhaven City</p>

    <div class="rule" style="top:865px"></div>
    <p class="abs italic follow-line">An evening of celebration to follow…</p>
    <div class="rule" style="top:933px"></div>

    <div class="ornament bottom" role="img" aria-label="Decorative heart flourish"></div>
  </section>
</div>
</body>
</html>
```